Pelling Home Efficiency

Id like for my business card to be very bold and professional. Incorporating the business logo, the main services offered, and my contact info. Services are spray foam, insulation, new construction, retrofit, weatherization.

When opening this project art huddle was not able to upload my new logo that I picked from another recent art huddle project. Does anyone know how i could upload my logo onto the page for design of the business cards?

Target Market(s)

Building owners, contractors

Industry/Entity Type

Building Insulation and performance improvements

Contact Information for Business Card

Owner, Email marcus@pellinghomeefficiency.com Phone number 555-204-6817

Colors
0054AA
0677BA
7BADD7
CADEEF
E8F1F8
F0912C
F2A743
F7CA91
FBE8D2
FDF5EE

Requirements
Must have
• Services- spray foam, cellulose, mineral wool, fiberglass, air sealing, new construction, retrofit, weatherization, energy saving assesments

```html
<!DOCTYPE html>
<html lang="en">
<head>
<meta charset="utf-8">
<title>Pelling Home Efficiency – Business Card</title>
<link rel="stylesheet" href="https://fonts.googleapis.com/css2?family=Poppins:wght@300;400;500;700;800&display=swap">
<style>
  :root{
    --navy:#0d1c4a;
    --navy-deep:#081538;
    --navy-light:#14307a;
    --cyan:#4cc3e6;
    --cyan-pale:#cadeef;
    --orange:#f0912c;
    --peach:#fbe8d2;
    --white:#ffffff;
    --paper:#f3f4f6;
    --stage:#e6e8ec;
  }
  *{margin:0;padding:0;box-sizing:border-box}
  html,body{width:1200px;height:917px;overflow:hidden;background:var(--stage);font-family:"Poppins",sans-serif}
  .canvas{position:relative;width:1200px;height:917px}
  .card{position:absolute;left:320px;width:560px;height:320px;overflow:hidden;border-radius:4px;box-shadow:0 10px 26px rgba(8,21,56,.25)}
  .card--front{top:118px;background:var(--paper)}
  .card--back{top:479px;background:radial-gradient(ellipse at 60% 40%,var(--navy-light),var(--navy-deep) 75%)}
  .front__top{position:absolute;left:0;top:0;width:560px;height:118px;background:var(--navy)}
  .front__rule{position:absolute;left:36px;top:84px;width:330px;height:4px;background:var(--cyan)}
  .front__band{position:absolute;left:0;bottom:0;width:560px;height:14px;background:var(--cyan)}
  .front__illustration{position:absolute;left:22px;top:134px;width:104px;height:158px;border-radius:3px;background:linear-gradient(160deg,var(--cyan) 0%,var(--cyan-pale) 100%)}
  .front__watermark{position:absolute;left:400px;top:132px;width:140px;height:160px;border-radius:70px 70px 8px 8px;background:var(--peach);opacity:.7}
  .brand{position:absolute;display:flex;align-items:center;gap:12px}
  .brand__mark{width:22px;height:22px;background:var(--cyan)}
  .brand__name{color:var(--orange);font-weight:800;text-transform:uppercase;letter-spacing:.5px;line-height:1}
  .card--front .brand{left:36px;top:42px}
  .card--front .brand__name{font-size:24px}
  .identity{position:absolute;left:150px;top:150px}
  .identity__name{color:var(--orange);font-weight:700;font-size:20px;letter-spacing:.5px;text-transform:uppercase;line-height:1.1}
  .identity__role{color:var(--cyan);font-weight:300;font-size:16px}
  .contact{position:absolute;left:150px;top:214px;list-style:none}
  .contact li{display:flex;align-items:center;gap:9px;color:var(--navy);font-size:14px;line-height:24px}
  .contact svg{width:16px;height:16px;flex:none}
  .contact__web{padding-left:25px}
  .card--back .brand{left:0;right:0;top:62px;justify-content:center}
  .card--back .brand__name{font-size:26px}
  .rule{position:absolute;left:110px;right:110px;top:108px;height:4px;background:var(--cyan)}
  .services{position:absolute;left:0;right:0;top:138px;text-align:center}
  .services__title{color:var(--orange);font-weight:700;font-size:19px;letter-spacing:1px;text-transform:uppercase;margin-bottom:10px}
  .services__line{color:var(--white);font-size:15px;line-height:26px}
  .dot{color:var(--orange);margin:0 5px}
</style>
</head>
<body>
<main class="canvas">

  <section class="card card--front">
    <div class="front__top"></div>
    <div class="front__rule"></div>
    <div class="front__illustration" role="img" aria-label="House roofline illustration with chimney and window"></div>
    <div class="front__watermark" role="img" aria-label="Faint large brand mark decoration"></div>
    <div class="front__band"></div>

    <div class="brand">
      <span class="brand__mark"></span>
      <span class="brand__name">Pelling Home Efficiency</span>
    </div>

    <div class="identity">
      <div class="identity__name">Dana Pelling</div>
      <div class="identity__role">Owner</div>
    </div>

    <ul class="contact">
      <li>
        <svg viewBox="0 0 16 16" aria-hidden="true"><circle cx="8" cy="8" r="8" fill="var(--orange)"/><rect x="5.5" y="3.5" width="5" height="9" rx="1" fill="none" stroke="#fff" stroke-width="1.2"/></svg>
        555-204-6817
      </li>
      <li>
        <svg viewBox="0 0 16 16" aria-hidden="true"><circle cx="8" cy="8" r="8" fill="var(--orange)"/><rect x="4" y="5" width="8" height="6" fill="none" stroke="#fff" stroke-width="1.2"/><path d="M4 5 L8 8.5 L12 5" fill="none" stroke="#fff" stroke-width="1.2"/></svg>
        marcus@pellinghomeefficiency.com
      </li>
      <li class="contact__web">pellinghomeefficiency.com</li>
    </ul>
  </section>

  <section class="card card--back">
    <div class="brand">
      <span class="brand__mark"></span>
      <span class="brand__name">Pelling Home Efficiency</span>
    </div>
    <div class="rule"></div>
    <div class="services">
      <h2 class="services__title">Services</h2>
      <p class="services__line"><span class="dot">•</span>spray foam<span class="dot">•</span>cellulose<span class="dot">•</span>mineral wool<span class="dot">•</span>fiberglass</p>
      <p class="services__line"><span class="dot">•</span>air sealing<span class="dot">•</span>new construction<span class="dot">•</span>retrofit<span class="dot">•</span>weatherization</p>
      <p class="services__line"><span class="dot">•</span>energy saving assesments</p>
    </div>
  </section>

</main>
</body>
</html>
```